Business card for Autism Consultancy

I need a double-sided business card for Brightpath Learning Consultancy
Please try to use the colours and graphics in line with our website www.brightpathlearn.nz
Front side
Logo and the name of the company – Brightpath Learning Consultancy
We use Child-Centred, Modern and Innovative approaches
Teaching autistic children to bond, laugh and play
www.brightpathlearn.nz
info@brightpathlearn.nz
phone +64 09 37 615 48
Back side
Photo
Mirela Dunstan
Founder
Postgraduate Autism (Children) Specialist (with Merit)
Qualified by the Faculty of Learning Support and Access Studies (FLSA), Harwell Vale University
mirela@brightpathlearn.nz
phone +64 937 615 48
mobile: +64 20 6283 9150
Please do not convert the text fields to outlines, i.e. I need to be able to edit any text after.
The final design should be either in Adobe Illustrator or Adobe Photoshop format.
The Specs for the business card are:
Full Bleed Size
94 x 58 mm
1110 x 685 pixels
Document Trim Size
91 x 55 mm
1075 x 650 pixels

```html
<!DOCTYPE html>
<html lang="en">
<head>
<meta charset="utf-8">
<title>Brightpath Learning Consultancy – Business Card</title>
<link rel="stylesheet" href="https://fonts.googleapis.com/css2?family=Kelly+Slab&family=Nunito:wght@400;600&display=swap">
<style>
  :root {
    --teal: #52c3bd;
    --teal-deep: #3fb9b2;
    --navy: #1f2a4f;
    --grey-text: #9a9a9a;
    --coral: #ee6a5a;
    --card: #ffffff;
    --stage: #ececec;
    --sun: #f7cf2a;
  }
  * { box-sizing: border-box; margin: 0; padding: 0; }
  html, body { width: 1119px; height: 1200px; overflow: hidden; }
  body {
    background: var(--stage);
    font-family: "Nunito", sans-serif;
    color: var(--navy);
    position: relative;
  }
  .card {
    position: absolute;
    left: 120px;
    width: 880px;
    height: 530px;
    background: var(--card);
    border-radius: 14px;
    overflow: hidden;
    box-shadow: 0 3px 10px rgba(0,0,0,0.18);
  }
  .card--person { top: 50px; }
  .card--company { top: 620px; }

  /* Person side */
  .side-panel {
    position: absolute; left: 0; top: 0;
    width: 365px; height: 100%;
    background: var(--teal);
  }
  .portrait {
    position: absolute;
    left: 54px; top: 43px;
    width: 248px; height: 248px;
    border-radius: 50%;
    background: radial-gradient(circle at 50% 45%, #e6b99c 0%, #c58d6c 35%, #6b4a35 70%, #f4f1ee 100%);
  }
  .person-name {
    position: absolute; left: 408px; top: 52px;
    font-family: "Kelly Slab", serif;
    font-size: 50px; line-height: 1;
    color: var(--navy);
    letter-spacing: 1px;
  }
  .person-role {
    position: absolute; left: 410px; top: 106px;
    font-family: "Kelly Slab", serif;
    font-size: 26px; line-height: 1;
    color: var(--teal-deep);
  }
  .person-title {
    position: absolute; left: 410px; top: 142px;
    font-size: 22px; line-height: 30px;
    font-weight: 600;
    color: var(--navy);
  }
  .person-qualification {
    position: absolute; left: 410px; top: 212px;
    font-size: 18px; line-height: 25px;
    color: var(--grey-text);
    width: 440px;
  }
  .contact-list {
    position: absolute;
    list-style: none;
    font-size: 25px;
    font-weight: 600;
    color: var(--navy);
  }
  .contact-list li {
    display: flex; align-items: center;
    height: 41px;
  }
  .contact-list svg { flex: none; }
  .card--person .contact-list { left: 420px; top: 380px; }
  .card--person .contact-list svg { margin-right: 14px; }

  /* Company side */
  .brand {
    position: absolute; left: 0; top: 180px;
    width: 100%;
    display: flex; align-items: center; justify-content: center;
    gap: 18px;
  }
  .brand-dot {
    width: 34px; height: 34px; border-radius: 50%;
    background: var(--sun);
  }
  .brand-name {
    font-family: "Kelly Slab", serif;
    font-size: 44px; line-height: 1;
    color: var(--navy);
  }
  .card--company .contact-list { left: 273px; top: 380px; }
  .card--company .contact-list svg { margin-right: 14px; }
  .card--company .contact-list .phone-number { margin-left: 24px; }
  .web-band {
    position: absolute; left: 0; bottom: 0;
    width: 880px; height: 52px;
  }
  .web-address {
    position: absolute; left: 252px; width: 376px;
    bottom: 14px;
    text-align: center;
    font-size: 23px; font-weight: 600;
    color: #fff;
  }
</style>
</head>
<body>

<section class="card card--person" aria-label="Card side with founder details">
  <div class="side-panel">
    <div class="portrait" role="img" aria-label="Portrait photo of Mirela Dunstan"></div>
  </div>
  <h1 class="person-name">Mirela Dunstan</h1>
  <p class="person-role">Founder</p>
  <p class="person-title">Postgraduate Autism (Children)<br>Specialist (with Merit)</p>
  <p class="person-qualification">Qualified by the Faculty of Learning Support and Access Studies (FLSA), Harwell Vale University</p>
  <ul class="contact-list">
    <li>
      <svg width="26" height="20" viewBox="0 0 26 20" aria-hidden="true"><rect x="1.5" y="1.5" width="23" height="17" rx="1.5" fill="none" stroke="#ee6a5a" stroke-width="2"/><polyline points="2,3 13,11 24,3" fill="none" stroke="#ee6a5a" stroke-width="2"/></svg>
      mirela@brightpathlearn.nz
    </li>
    <li>
      <svg width="26" height="28" viewBox="0 0 26 28" aria-hidden="true"><rect x="5" y="1.5" width="16" height="25" rx="2.5" fill="none" stroke="#ee6a5a" stroke-width="2"/><circle cx="13" cy="22" r="1.4" fill="#ee6a5a"/></svg>
      +64 20 6283 9150
    </li>
  </ul>
</section>

<section class="card card--company" aria-label="Card side with company details">
  <div class="brand">
    <span class="brand-dot" aria-hidden="true"></span>
    <span class="brand-name">Brightpath Learning Consultancy</span>
  </div>
  <ul class="contact-list">
    <li>
      <svg width="26" height="20" viewBox="0 0 26 20" aria-hidden="true"><rect x="1.5" y="1.5" width="23" height="17" rx="1.5" fill="none" stroke="#ee6a5a" stroke-width="2"/><polyline points="2,3 13,11 24,3" fill="none" stroke="#ee6a5a" stroke-width="2"/></svg>
      info@brightpathlearn.nz
    </li>
    <li>
      <svg width="26" height="26" viewBox="0 0 26 26" aria-hidden="true"><path d="M6 3 L10 3 L12 9 L9 11 Q11 16 15 18 L17 15 L23 17 L23 21 Q22 24 19 24 Q10 23 5 15 Q2 9 3 6 Q4 3 6 3 Z" fill="none" stroke="#ee6a5a" stroke-width="1.8" stroke-linejoin="round"/><path d="M15 3 Q22 4 23 11 M15 7 Q19 8 19 11" fill="none" stroke="#ee6a5a" stroke-width="1.6" stroke-linecap="round"/></svg>
      <span class="phone-number">+64 09 37 615 48</span>
    </li>
  </ul>
  <svg class="web-band" viewBox="0 0 880 52" aria-hidden="true">
    <rect x="0" y="32" width="880" height="20" fill="#52c3bd"/>
    <path d="M238 52 L250 6 Q252 0 259 0 L621 0 Q628 0 630 6 L642 52 Z" fill="#52c3bd"/>
  </svg>
  <p class="web-address">www.brightpathlearn.nz</p>
</section>

</body>
</html>
```